RKW Automotive needs a catchy banner design

We need a design for a banner to be displayed on the fence in the outfield of a baseball stadium to show off our company and have people interested in what we do. We need something catchy that's going to attract people to look over at our banner.
We are a
Complete Automotive Service Company
Tires - Service - Repair - Diesel
We are in a Town called Fuquay-Varina
(555)314-2096 we would like the phone number to be a descent size so when you are in the stands you can read it.
I have attached what we came up with but like I said we need it to pop more and make the viewer that's looking at it want to look us up.
The Banner size is 24ft long and 10ft tall

```html
<!DOCTYPE html>
<html lang="en">
<head>
<meta charset="utf-8">
<title>RKW Automotive – Outfield Banner</title>
<link rel="stylesheet" href="https://fonts.googleapis.com/css2?family=Cabin:wght@700&family=Arimo:wght@700&family=Roboto:wght@500;700&display=swap">
<style>
  :root {
    --page-bg: #ffffff;
    --banner-blue: #0a63c4;
    --stripe-blue: #3a93f2;
    --panel-dark: #343436;
    --panel-frame: #9b9b9d;
    --text-white: #ffffff;
    --text-yellow: #fff21a;
    --brand-blue: #2b8ff2;
  }
  html, body {
    margin: 0;
    width: 1200px;
    height: 561px;
    overflow: hidden;
    background: var(--page-bg);
  }
  .banner {
    display: block;
    width: 1200px;
    height: 561px;
  }
  .banner-field { fill: var(--banner-blue); }
  .banner-stripe { fill: var(--stripe-blue); }
  .panel-frame { fill: var(--panel-frame); }
  .panel-body { fill: var(--panel-dark); }
  .headline {
    font-family: "Cabin", "Gill Sans", sans-serif;
    font-weight: 700;
    font-size: 52px;
    fill: var(--text-white);
  }
  .town {
    font-family: "Arimo", Arial, sans-serif;
    font-weight: 700;
    font-size: 52px;
    fill: var(--text-yellow);
  }
  .tagline {
    font-family: "Cabin", "Gill Sans", sans-serif;
    font-weight: 700;
    font-size: 30px;
    fill: var(--text-white);
  }
  .services {
    font-family: "Cabin", "Gill Sans", sans-serif;
    font-weight: 700;
    font-size: 42px;
    fill: var(--text-yellow);
  }
  .service-dot { fill: var(--text-yellow); stroke: #ffffff; stroke-width: 1.5; }
  .phone {
    font-family: "Roboto", Arial, sans-serif;
    font-weight: 500;
    font-size: 128px;
    fill: var(--text-white);
  }
  .brand-name {
    font-family: "Cabin", "Gill Sans", sans-serif;
    font-weight: 700;
    fill: var(--brand-blue);
  }
</style>
</head>
<body>
<svg class="banner" viewBox="0 0 1200 561" xmlns="http://www.w3.org/2000/svg">
  <defs>
    <filter id="banner-shadow" x="-5%" y="-5%" width="110%" height="115%">
      <feDropShadow dx="2" dy="3" stdDeviation="3" flood-color="#000" flood-opacity="0.35"/>
    </filter>
  </defs>

  <g filter="url(#banner-shadow)">
    <rect class="banner-field" x="16" y="28" width="1170" height="488"/>
  </g>

  <rect class="banner-stripe" x="16" y="37" width="1170" height="7"/>
  <rect class="banner-stripe" x="16" y="128" width="1170" height="8"/>

  <polygon class="panel-frame" points="36,220 251,158 469,220 469,378 1186,378 1186,516 36,516"/>
  <polygon class="panel-body" points="47,228 251,170 458,228 458,389 1186,389 1186,516 47,516"/>

  <text class="headline" x="600" y="105" text-anchor="middle" textLength="1120" lengthAdjust="spacingAndGlyphs">Complete Automotive Service Company</text>

  <text class="town" x="1148" y="192" text-anchor="end" textLength="393" lengthAdjust="spacingAndGlyphs">Fuquay-Varina</text>

  <text class="tagline" x="511" y="281" textLength="572" lengthAdjust="spacingAndGlyphs">From Oil Changes To Custom Builds</text>

  <g class="service-list">
    <rect class="service-dot" x="485" y="331" width="8" height="8" transform="rotate(45 489 335)"/>
    <text class="services" x="505" y="351" textLength="110" lengthAdjust="spacingAndGlyphs">Tires</text>
    <rect class="service-dot" x="631" y="331" width="8" height="8" transform="rotate(45 635 335)"/>
    <text class="services" x="651" y="351" textLength="161" lengthAdjust="spacingAndGlyphs">Service</text>
    <rect class="service-dot" x="828" y="331" width="8" height="8" transform="rotate(45 832 335)"/>
    <text class="services" x="848" y="351" textLength="145" lengthAdjust="spacingAndGlyphs">Repair</text>
    <rect class="service-dot" x="1009" y="331" width="8" height="8" transform="rotate(45 1013 335)"/>
    <text class="services" x="1029" y="351" textLength="138" lengthAdjust="spacingAndGlyphs">Diesel</text>
  </g>

  <text class="phone" x="494" y="492" textLength="669" lengthAdjust="spacingAndGlyphs">(555)314-2096</text>

  <g class="brand">
    <text class="brand-name" x="253" y="335" text-anchor="middle" font-size="92" textLength="260" lengthAdjust="spacingAndGlyphs">RKW</text>
    <text class="brand-name" x="253" y="395" text-anchor="middle" font-size="44" textLength="260" lengthAdjust="spacingAndGlyphs">Automotive</text>
  </g>
</svg>
</body>
</html>
```